Makeup Artist

Hi I am makeup artist I attached the business card that I found on the net love the design.
I would love something like this simple but looking expensive.
I want double side business card. Front my full name. my phone number, email address and facebook and my next appointment is... on the other side.
Thank you :)

Hello I change my Facebook account - Makeup by Kolina, if you could please update your designs , thank you

Target Market(s)

high end clientele

Industry/Entity Type

Business

Colors
ec2027
ffc214
33b7a4
6b449b
e34197
9bcb3c
f37122
a64599

Requirements
Must have
• bright colours
Should not have
• brushes or whole lipsticks

```html
<!DOCTYPE html>
<html lang="en">
<head>
<meta charset="utf-8">
<title>Kolina Marveau – Makeup Artist Business Card</title>
<link href="https://fonts.googleapis.com/css2?family=Indie+Flower&family=Open+Sans:ital,wght@0,400;0,700;1,700&display=swap" rel="stylesheet">
<style>
  :root {
    --page: #efece5;
    --card-front: #edf3fb;
    --card-band: #f6f9fe;
    --card-back: #ffffff;
    --pink: #e0218a;
    --magenta: #b3309c;
    --purple: #6b449b;
    --violet: #8e4aa6;
    --red: #d4302b;
    --orange: #f37122;
    --green: #2fae4a;
    --fb-square: #3b5ba5;
  }
  * { margin: 0; padding: 0; box-sizing: border-box; }
  html, body { width: 927px; height: 1200px; overflow: hidden; }
  body { background: var(--page); position: relative; font-family: "Open Sans", Arial, sans-serif; }

  .card { position: absolute; left: 170px; width: 661px; height: 387px; overflow: hidden; }
  .card--front { top: 185px; background: var(--card-front); }
  .card--back { top: 671px; background: var(--card-back); }

  .front__band { position: absolute; left: 0; right: 0; top: 45px; height: 80px; background: var(--card-band); }
  .front__art {
    position: absolute; left: 0; top: 0; width: 290px; height: 387px;
    background: linear-gradient(90deg, #c99ad6 0%, #e2a7cb 40%, #bcdcd3 68%, rgba(237,243,251,0) 100%);
  }
  .front__name {
    position: absolute; left: 300px; top: 54px; line-height: 40px;
    font-family: "Indie Flower", cursive; font-size: 29px; color: var(--pink); letter-spacing: 0.5px;
  }
  .front__role {
    position: absolute; right: 96px; top: 88px; line-height: 30px;
    font-weight: 700; font-style: italic; font-size: 21px; color: var(--magenta);
  }
  .contact { position: absolute; left: 222px; top: 170px; }
  .contact__rule { position: absolute; left: 42px; top: 0; width: 3px; height: 118px; background: var(--orange); }
  .contact__row { display: flex; align-items: center; height: 37px; }
  .contact__icon { width: 30px; height: 26px; margin-right: 22px; display: flex; justify-content: center; align-items: center; }
  .contact__text { font-size: 25px; color: var(--violet); }
  .contact__square { width: 22px; height: 22px; background: var(--fb-square); border-radius: 3px; }

  .back__prompt { position: absolute; left: 36px; top: 56px; font-weight: 700; font-size: 19px; color: var(--purple); }
  .back__field { position: absolute; left: 57px; font-size: 18px; color: var(--red); display: flex; align-items: flex-end; }
  .back__field--date { top: 110px; }
  .back__field--time { top: 146px; }
  .back__line { display: inline-block; height: 20px; border-bottom: 1.5px solid var(--red); margin-left: 6px; }
  .back__swatch {
    position: absolute; left: 388px; top: 76px; width: 252px; height: 110px;
    background: var(--pink);
  }
  .back__note {
    position: absolute; left: 0; right: 0; top: 244px; text-align: center; padding-right: 10px;
    font-family: "Indie Flower", cursive; font-size: 27px; line-height: 36px; color: var(--pink);
  }
</style>
</head>
<body>
  <section class="card card--front" aria-label="Business card front">
    <div class="front__band"></div>
    <div class="front__art" role="img" aria-label="Photograph of scattered crushed colourful eyeshadow pieces"></div>
    <div class="front__name">Kolina Marveau</div>
    <div class="front__role">Makeup Artist</div>
    <div class="contact">
      <div class="contact__rule"></div>
      <div class="contact__row">
        <span class="contact__icon">
          <svg width="30" height="26" viewBox="0 0 30 26" aria-hidden="true">
            <path d="M2 9 Q15 0 28 9 L28 12 L22 12 L21 8 Q15 6 9 8 L8 12 L2 12 Z" fill="#6b449b"/>
            <path d="M7 13 L10 9 L20 9 L23 13 L26 24 L4 24 Z" fill="#6b449b"/>
            <circle cx="15" cy="17" r="4" fill="#edf3fb"/>
            <circle cx="15" cy="17" r="1.6" fill="#6b449b"/>
          </svg>
        </span>
        <span class="contact__text">042.555.0148</span>
      </div>
      <div class="contact__row">
        <span class="contact__icon"><span class="contact__square"></span></span>
        <span class="contact__text">Makeup by Kolina</span>
      </div>
      <div class="contact__row">
        <span class="contact__icon">
          <svg width="28" height="22" viewBox="0 0 28 22" aria-hidden="true">
            <rect x="0" y="0" width="28" height="22" rx="2" fill="#2fae4a"/>
            <path d="M2 3 L14 13 L26 3 M2 19 L11 11 M26 19 L17 11" stroke="#fff" stroke-width="2" fill="none"/>
          </svg>
        </span>
        <span class="contact__text">kolina.marveau@mail.com</span>
      </div>
    </div>
  </section>

  <section class="card card--back" aria-label="Business card back">
    <div class="back__prompt">My next appointment is....</div>
    <div class="back__field back__field--date">Date:<span class="back__line" style="width:196px"></span></div>
    <div class="back__field back__field--time">Time:<span class="back__line" style="width:198px"></span></div>
    <div class="back__swatch" role="img" aria-label="Photograph of a bright pink lipstick smear"></div>
    <p class="back__note">Looking forward to our<br>appointment!</p>
  </section>
</body>
</html>
```